8.5 x 11" Funny Poster - "In case of Alien Invasion..."

We sell data backup services to small business customers which is sometimes "too serious". We're creating a campaign to focus on a more light hearted way to draw customer's attention.
The Poster should seek to use imagery that is funny and light hearted -- be creative. It needs to draw attention and get the reader to chuckle.
Our products are sold in computer stores -- so we're looking to create an 8.5" x 11" Tabletop Sign to be displayed as an instore display. We'll be using Printwell to print the signs, their product specifications with bleeds and margins are documented on their website at:
http://www.printwell-example.com/signs-and-banners/signs/table-top-signs
The copy for the poster is attached in both Word and pdf formats. We'd like a small version of our logo to be included somewhere on the flyer (attached is a Illustrator and JPG version of our logo). We'd also like to include our url http://brindlex.net.
The finished product should be Adobe Illustrator CS3 (*.ai) with a PDF Proof.
retail small business
Business
Designer to choose colors to be used in the design.

```html
<!DOCTYPE html>
<html lang="en">
<head>
<meta charset="utf-8">
<title>In Case of Alien Invasion – Brindlex Net</title>
<link rel="stylesheet" href="https://fonts.googleapis.com/css2?family=Luckiest+Guy&display=swap">
<style>
  :root {
    --sky-center: #00c4f4;
    --sky-mid: #0aa6d6;
    --sky-edge: #0b6785;
    --ink: #ffffff;
    --shade: rgba(0, 40, 60, 0.55);
  }
  html, body {
    margin: 0;
    padding: 0;
    width: 927px;
    height: 1200px;
    overflow: hidden;
    background: var(--sky-edge);
  }
  .poster {
    display: block;
    width: 927px;
    height: 1200px;
  }
  .headline {
    font-family: "Luckiest Guy", "Arial Black", sans-serif;
    fill: var(--ink);
    filter: drop-shadow(0 3px 6px var(--shade));
  }
  .brand-name {
    font-family: "Luckiest Guy", "Arial Black", sans-serif;
    fill: var(--ink);
  }
  .brand-mark {
    fill: var(--ink);
  }
  .credit {
    font-family: "Luckiest Guy", "Arial Black", sans-serif;
    fill: var(--ink);
    letter-spacing: 1px;
  }
</style>
</head>
<body>
<svg class="poster" viewBox="0 0 927 1200" xmlns="http://www.w3.org/2000/svg">
  <defs>
    <radialGradient id="sky" cx="50%" cy="48%" r="70%">
      <stop offset="0%" stop-color="var(--sky-center)"/>
      <stop offset="55%" stop-color="var(--sky-mid)"/>
      <stop offset="100%" stop-color="var(--sky-edge)"/>
    </radialGradient>
    <linearGradient id="fleet-tone" x1="0" y1="0" x2="0" y2="1">
      <stop offset="0%" stop-color="#ffffff" stop-opacity="0.35"/>
      <stop offset="100%" stop-color="#ffffff" stop-opacity="0.2"/>
    </linearGradient>
  </defs>

  <rect class="sky" width="927" height="1200" fill="url(#sky)"/>

  <g class="warning">
    <text class="headline" x="22" y="80" font-size="82" textLength="882" lengthAdjust="spacingAndGlyphs">IN CASE OF ALIEN INVASION</text>
    <text class="headline" x="22" y="160" font-size="76" textLength="888" lengthAdjust="spacingAndGlyphs">SAVE THE CHILDREN, THE PETS</text>
    <text class="headline" x="22" y="260" font-size="98" textLength="884" lengthAdjust="spacingAndGlyphs">AND YOUR COMPUTER</text>
    <text class="headline" x="22" y="400" font-size="168" textLength="882" lengthAdjust="spacingAndGlyphs">LEAVE GRANNY</text>
  </g>

  <rect class="ufo-fleet" x="22" y="456" width="878" height="204" rx="40" fill="url(#fleet-tone)"
        role="img" aria-label="Illustration of a fleet of white flying saucers crossing the sky"/>

  <g class="punchline">
    <text class="headline" x="16" y="776" font-size="106" textLength="894" lengthAdjust="spacingAndGlyphs">ON SECOND THOUGHT</text>
    <text class="headline" x="35" y="872" font-size="95" textLength="863" lengthAdjust="spacingAndGlyphs">BACKUP WITH BRINDLEX NET,</text>
    <text class="headline" x="22" y="952" font-size="80" textLength="888" lengthAdjust="spacingAndGlyphs">AND FORGET THE COMPUTER</text>
    <text class="headline" x="22" y="1104" font-size="176" textLength="888" lengthAdjust="spacingAndGlyphs">SAVE GRANNY!</text>
  </g>

  <g class="sign-off">
    <g class="brand">
      <circle class="brand-mark" cx="36" cy="1150" r="10"/>
      <text class="brand-name" x="54" y="1164" font-size="38" textLength="222" lengthAdjust="spacingAndGlyphs">BrindlexNet</text>
    </g>
    <text class="credit" x="293" y="1152" font-size="33" textLength="613" lengthAdjust="spacingAndGlyphs">BROUGHT TO YOU BY BRINDLEX NET, INC.</text>
    <text class="credit" x="293" y="1180" font-size="24" textLength="623" lengthAdjust="spacingAndGlyphs">SAVING THE PLANET FROM ALIEN INVASION SINCE 1994.</text>
  </g>
</svg>
</body>
</html>
```